Buisness Card Sationary
Les Sentiers Bleus
Karim BELLAHCENE
Directeur Générale
Centre Commercial et d’Affaire Ennakhil Bureau 2604 Cheraga, Alger Algérie
Karim.BELLAHCENE@sahelreseau.com
www.SahelReseau.com
Logo with or without the Map

```html
<!DOCTYPE html>
<html lang="fr">
<head>
<meta charset="utf-8">
<title>Les Sentiers Bleus — Papeterie</title>
<link href="https://fonts.googleapis.com/css2?family=Open+Sans:wght@400;600;700&display=swap" rel="stylesheet">
<style>
  :root{
    --ground:#ece7df;
    --paper:#ffffff;
    --green:#1f5a3c;
    --ink:#3c3c3c;
    --muted:#8a8a8a;
    --rule:#b9b9b9;
  }
  *{box-sizing:border-box;margin:0;padding:0}
  html,body{width:1200px;height:576px;overflow:hidden}
  body{background:var(--ground);font-family:"Open Sans",Arial,sans-serif;color:var(--ink);position:relative}
  .sheet,.card,.envelope{position:absolute;background:var(--paper);box-shadow:0 2px 6px rgba(0,0,0,.18);overflow:hidden}
  .corner{position:absolute;top:0;right:0}
  .brand{position:absolute;font-weight:600;color:var(--green);white-space:nowrap}
  .brand-dot{display:inline-block;width:.55em;height:.55em;border-radius:50%;background:var(--green);margin-right:.35em;vertical-align:.05em}

  /* A4 sheets */
  .sheet{top:36px;width:336px;height:504px}
  .sheet--fax{left:53px}
  .sheet--letter{left:427px}
  .sheet .brand{left:34px;top:34px;font-size:13px}
  .fax-title{position:absolute;left:34px;top:96px;font-size:17px;font-weight:600;letter-spacing:1px}
  .fax-fields{position:absolute;left:34px;top:128px;width:268px;display:grid;grid-template-columns:1fr 1fr;column-gap:22px;row-gap:11px}
  .fax-field{border-bottom:1px solid var(--rule);font-size:5.5px;color:var(--muted);padding-bottom:2px;height:12px}
  .fax-options{position:absolute;left:34px;top:236px;display:flex;gap:12px;font-size:5px;color:var(--muted)}
  .fax-options span::before{content:"";display:inline-block;width:5px;height:5px;border:1px solid var(--rule);margin-right:3px;vertical-align:-1px}
  .sheet-footer{position:absolute;left:34px;bottom:26px;font-size:4.6px;line-height:1.6;color:var(--muted);white-space:nowrap}

  /* Business cards */
  .card{top:77px;width:139px;height:84px}
  .card--front{left:802px}
  .card--back{left:955px}
  .card .brand{font-size:8px}
  .card--front .brand{left:9px;top:11px}
  .card-lines{position:absolute;left:9px;top:34px;width:64px;font-size:3.5px;line-height:1.7;color:var(--muted);white-space:nowrap}
  .card-person{position:absolute;left:80px;top:34px;width:54px;font-size:3.5px;line-height:1.7;color:var(--ink);white-space:nowrap}
  .card-person strong{display:block;font-weight:700;font-size:4.4px;line-height:1.4;color:var(--green)}
  .card--back .brand{left:14px;top:30px}

  /* Envelope */
  .envelope{left:802px;width:292px}
  .envelope--front{top:211px;height:154px}
  .envelope--front .brand{left:18px;top:22px;font-size:12px}
  .envelope--front .sheet-footer{left:18px;bottom:auto;top:88px;font-size:3.8px}
  .envelope--back{top:377px;height:165px}
  .flap{position:absolute;left:0;top:0}
  .envelope--back .brand{left:0;width:292px;text-align:center;top:26px;font-size:8px;color:#fff}
</style>
</head>
<body>

<section class="sheet sheet--fax">
  <svg class="corner" width="120" height="72" viewBox="0 0 120 72"><path d="M0 0H120V72Q70 64 40 30Q22 12 0 0Z" fill="var(--green)"/></svg>
  <div class="brand"><span class="brand-dot"></span>Les Sentiers Bleus</div>
  <h1 class="fax-title">FAX</h1>
  <div class="fax-fields">
    <div class="fax-field">To :</div><div class="fax-field">From :</div>
    <div class="fax-field">Fax :</div><div class="fax-field">Pages :</div>
    <div class="fax-field">Phone :</div><div class="fax-field">Date :</div>
    <div class="fax-field">Re :</div><div class="fax-field">CC :</div>
  </div>
  <div class="fax-options">
    <span>Urgent</span><span>For Review</span><span>Please Comment</span><span>Please Reply</span><span>Please Recycle</span>
  </div>
  <div class="sheet-footer">
    Centre Commercial et d’Affaire Ennakhil Bureau 2604 Cheraga, Alger Algérie<br>
    Tél : +213 (0) 21 45 67 89 &nbsp; Fax : +213 (0) 21 45 67 90<br>
    Karim.BELLAHCENE@sahelreseau.com &nbsp; www.SahelReseau.com
  </div>
</section>

<section class="sheet sheet--letter">
  <svg class="corner" width="120" height="72" viewBox="0 0 120 72"><path d="M0 0H120V72Q70 64 40 30Q22 12 0 0Z" fill="var(--green)"/></svg>
  <div class="brand"><span class="brand-dot"></span>Les Sentiers Bleus</div>
  <div class="sheet-footer">
    Centre Commercial et d’Affaire Ennakhil Bureau 2604 Cheraga, Alger Algérie<br>
    Tél : +213 (0) 21 45 67 89 &nbsp; Fax : +213 (0) 21 45 67 90<br>
    Karim.BELLAHCENE@sahelreseau.com &nbsp; www.SahelReseau.com
  </div>
</section>

<section class="card card--front">
  <svg class="corner" width="52" height="34" viewBox="0 0 52 34"><path d="M0 0H52V34Q30 30 18 14Q10 5 0 0Z" fill="var(--green)"/></svg>
  <div class="brand"><span class="brand-dot"></span>Les Sentiers Bleus</div>
  <div class="card-lines">
    Centre Commercial et d’Affaire<br>
    Ennakhil Bureau 2604<br>
    Cheraga, Alger Algérie<br>
    Karim.BELLAHCENE@sahelreseau.com<br>
    www.SahelReseau.com
  </div>
  <div class="card-person">
    <strong>Karim BELLAHCENE</strong>
    Directeur Générale<br>
    Mob : +213 (0) 770 12 34 56
  </div>
</section>

<section class="card card--back">
  <svg class="corner" width="52" height="34" viewBox="0 0 52 34"><path d="M0 0H52V34Q30 30 18 14Q10 5 0 0Z" fill="var(--green)"/></svg>
  <div class="brand"><span class="brand-dot"></span>Les Sentiers Bleus</div>
</section>

<section class="envelope envelope--front">
  <svg class="corner" width="104" height="64" viewBox="0 0 104 64"><path d="M0 0H104V64Q60 56 34 26Q18 10 0 0Z" fill="var(--green)"/></svg>
  <div class="brand"><span class="brand-dot"></span>Les Sentiers Bleus</div>
  <div class="sheet-footer">
    Centre Commercial et d’Affaire Ennakhil Bureau 2604 Cheraga, Alger Algérie<br>
    www.SahelReseau.com
  </div>
</section>

<section class="envelope envelope--back">
  <svg class="flap" width="292" height="62" viewBox="0 0 292 62"><path d="M0 0H292V22Q146 72 0 22Z" fill="var(--green)"/></svg>
  <div class="brand">Les Sentiers Bleus</div>
</section>

</body>
</html>
```